Ethical Dilemma - Case study poster

- Create a poster/infographic detailing a real-world case study where you, as a paramedic, have encountered a patient situation that poses an ethical dilemma.
- Discuss the following principles and how they relate to the case study: beneficence, autonomy, non-maleficence and justice.
- A0 size, either landscape or portrait. Please include one or two areas for images and/or tables and graphs with backup research.
- The font must be legible, at least 12 points and 1.5 spacing with a section for all five student names to be read on the poster.
-
Target Market(s)
Academic project
Industry/Entity Type
Paramedicine and ethics
Look and feel

```html
<!DOCTYPE html>
<html lang="en">
<head>
<meta charset="utf-8">
<title>Ethical Dilemma – Case Study Poster</title>
<link href="https://fonts.googleapis.com/css2?family=Montserrat:wght@800;900&family=Lato:wght@400;700&display=swap" rel="stylesheet">
<style>
  :root {
    --canvas: #efefef;
    --paper: #ffffff;
    --red: #e04e2b;
    --orange: #f7821f;
    --orange-head: #f58a1f;
    --purple: #9b2c7c;
    --pink: #c98fbf;
    --grey: #e9e9e9;
    --ink: #2b2b2b;
    --photo-a: #e7dcd2;
    --photo-b: #b69a86;
  }
  * { margin: 0; padding: 0; box-sizing: border-box; }
  html, body { width: 1200px; height: 1200px; overflow: hidden; background: var(--canvas); }
  .poster {
    position: absolute; left: 190px; top: 20px;
    width: 564px; height: 797px;
    transform: scale(1.455); transform-origin: 0 0;
    background: var(--paper);
    font-family: "Lato", Arial, sans-serif; color: var(--ink);
  }
  .poster-shapes { position: absolute; inset: 0; }
  .heading { font-family: "Montserrat", Arial, sans-serif; font-weight: 900; color: #fff; line-height: 0.95; position: absolute; text-transform: uppercase; }
  .poster-label { left: 18px; top: 9px; font-size: 19px; }
  .poster-title { left: 228px; top: 12px; font-size: 12.2px; font-weight: 800; line-height: 1.05; }
  .band-title { left: 0; width: 564px; top: 215px; text-align: center; font-size: 11.5px; font-weight: 800; }
  .photo { position: absolute; left: 0; top: 57px; width: 222px; height: 151px; background: linear-gradient(135deg, var(--photo-a), var(--photo-b)); }
  .body { position: absolute; font-size: 4.6px; line-height: 1.32; text-align: justify; }
  .case-text { left: 248px; top: 70px; width: 308px; }
  .case-text p + p { margin-top: 5px; }
  .placeholder { position: absolute; font-size: 4.6px; line-height: 1.2; text-transform: uppercase; }
  .on-dark { color: #fff; }
  .autonomy-text { left: 19px; top: 262px; width: 182px; }
  .autonomy-space { left: 19px; top: 328px; }
  .beneficence-text { left: 322px; top: 262px; width: 232px; text-align: center; }
  .beneficence-space { right: 14px; top: 300px; text-align: right; }
  .maleficence-text { left: 17px; top: 562px; width: 196px; text-align: left; }
  .maleficence-space { left: 17px; top: 605px; }
  .justice-text { left: 372px; top: 549px; width: 182px; text-align: right; }
  .justice-space { right: 11px; top: 594px; text-align: right; }
  .autonomy-label { left: 238px; top: 392px; font-size: 15px; color: var(--red); transform: rotate(-81deg); transform-origin: 0 0; }
  .beneficence-label { left: 397px; top: 466px; font-size: 17px; }
  .maleficence-label { left: 17px; top: 508px; font-size: 17px; line-height: 1.02; }
  .justice-label { left: 322px; top: 722px; font-size: 15px; transform: rotate(-81deg); transform-origin: 0 0; }
  .conclusion-label { left: 9px; top: 761px; font-size: 11.5px; font-weight: 800; }
  .conclusion-text { left: 146px; top: 742px; width: 408px; }
</style>
</head>
<body>
<main class="poster">
  <svg class="poster-shapes" width="564" height="797" viewBox="0 0 564 797" aria-hidden="true">
    <rect class="header-band" x="0" y="0" width="564" height="57" fill="var(--orange-head)"/>
    <polygon class="header-label-block" points="0,0 195,0 186,57 0,57" fill="var(--red)"/>
    <rect class="section-band" x="0" y="208" width="564" height="33" fill="var(--pink)"/>
    <polygon class="quad-autonomy" points="0,241 232,241 272,490 0,490" fill="var(--grey)"/>
    <polygon class="quad-beneficence" points="232,241 564,241 564,492 272,490" fill="var(--purple)"/>
    <polygon class="quad-maleficence" points="0,490 272,490 312,735 0,735" fill="var(--orange)"/>
    <polygon class="quad-justice" points="272,490 564,492 564,735 312,735" fill="var(--red)"/>
    <polygon class="conclusion-block" points="0,735 122,735 116,797 0,797" fill="var(--pink)"/>
    <g class="principle-wheel">
      <circle cx="271" cy="462" r="63" fill="#fff" opacity="0.35"/>
      <circle cx="271" cy="462" r="53" fill="#fff" opacity="0.85"/>
      <path d="M271,409 A53,53 0 0 1 324,462 L271,462 Z" fill="var(--purple)" opacity="0.18"/>
      <path d="M218,462 A53,53 0 0 0 271,515 L271,462 Z" fill="var(--orange)" opacity="0.18"/>
      <path d="M324,462 A53,53 0 0 1 271,515 L271,462 Z" fill="var(--red)" opacity="0.12"/>
      <!-- mind / reasoning icon -->
      <g fill="#d9529b">
        <circle cx="245" cy="438" r="12"/>
        <rect x="238" y="446" width="11" height="10"/>
      </g>
      <circle cx="246" cy="437" r="4" fill="#fff"/>
      <!-- care / support icon -->
      <g fill="var(--purple)">
        <circle cx="289" cy="428" r="4.5"/>
        <circle cx="301" cy="430" r="4.5"/>
        <path d="M283,436 h12 v20 h-4 v-12 h-4 v12 h-4 z"/>
        <path d="M296,438 h10 v18 h-4 v-10 h-3 z"/>
      </g>
      <!-- heart in hand icon -->
      <g fill="var(--orange)">
        <path d="M252,478 c-4,-6 -13,-2 -9,5 l9,9 l9,-9 c4,-7 -5,-11 -9,-5 z"/>
        <path d="M231,494 h8 v10 h-8 z"/>
        <path d="M241,495 h10 c4,0 4,4 0,4 h-6 h8 l10,-4 c3,-1 5,2 2,4 l-12,6 h-12 z"/>
      </g>
      <!-- scales icon -->
      <g stroke="var(--red)" stroke-width="1.6" fill="none">
        <line x1="293" y1="478" x2="293" y2="506"/>
        <line x1="280" y1="483" x2="306" y2="483"/>
        <line x1="285" y1="506" x2="301" y2="506"/>
        <path d="M280,483 l-5,11 h10 z M306,483 l-5,11 h10 z"/>
      </g>
    </g>
  </svg>

  <div class="heading poster-label">Ethical<br>Dilemma</div>
  <div class="heading poster-title">Challenging Family Dynamics<br>in an Emergency Setting</div>

  <div class="photo" role="img" aria-label="Photograph of a worried mother holding her distressed young daughter at home"></div>

  <div class="body case-text">
    <p>Responding to a distress call from a patient stating a drug overdose. Upon arriving, the patient's mother greets you at the door, concerned and anxious. The patient emerges from the house, looking distressed and is guided to the ambulance for initial observations. During the conversation, she admits to feeling suicidal and reveals that, at times, her parents have locked her in the garden shed. Concerned for her well-being, you impress the need to present to the hospital.</p>
    <p>The patient agrees to seek further help and returns to the hospital to collect some personal belongings. As she reappears, her mother by her side, there is a noticeable change in the atmosphere. Her mother appears tense and denies any issues. The patient's demeanour has also shifted, echoing her mother and denying thoughts of suicide and the apparent overdose. Her mother has now called the police. It is very clear that the family has tension and disagreement regarding their daughter's condition and the appropriate course of action for her medical needs.</p>
  </div>

  <div class="heading band-title">Application of Bioethical Principles</div>

  <div class="body autonomy-text">While the patient initially expressed her desire for medical help, her subsequent change of heart raises concerns. Her independence should be respected, but a careful assessment of her decision-making capacity is crucial, given the potential for external influence or mental health issues.</div>
  <div class="placeholder autonomy-space">Space for<br>additional text<br>graph, table</div>

  <div class="body beneficence-text on-dark">Given her history of suicidal thoughts and the conflicting messages, your primary responsibility is her well-being. Acting in her best interest is paramount if you suspect she's being coerced or manipulated</div>
  <div class="placeholder beneficence-space on-dark">Space for<br>additional text<br>graph, table</div>

  <div class="body maleficence-text on-dark">Your role is to ensure that her actions are not compromised by undue pressure or emotional manipulation from her mother. If you sense harm could come to her due to the situation, steps must be taken to protect her.</div>
  <div class="placeholder maleficence-space on-dark">Space for<br>additional text<br>graph, table</div>

  <div class="body justice-text on-dark">While considering the patient's mother's perspective, your ultimate priority remains the patient's welfare and safety. Balance her mother's role with your duty to safeguard the patient from harm.</div>
  <div class="placeholder justice-space on-dark">Space for<br>additional text<br>graph, table</div>

  <div class="heading autonomy-label">Autonomy</div>
  <div class="heading beneficence-label">Beneficence</div>
  <div class="heading maleficence-label">Non<br>Maleficence</div>
  <div class="heading justice-label">Justice</div>

  <div class="heading conclusion-label">Conclusion</div>
  <div class="body conclusion-text">The situation is complex, involving potential coercion, mental health concerns, and disagreement within the family. Collaboration with medical professionals and possibly involving the police might be necessary to ensure her safety and well-being. Although you should strive to honour the patient's autonomy, you have a duty to intervene if her current stance is influenced by factors that put her at risk. Ultimately, your actions should align with the principles of protecting her from harm and prioritising her overall welfare.</div>
</main>
</body>
</html>
```